Velvet Root Studio- An All Natural Hair & Skincare Company needs a website design.

Velvet Root Studio is an all-natural Hair & Skin Company that provides all natural hair and skin care products to the ever growing natural hair community. Our primary target market is African American women between the ages of 16-50. I would like my website to be setup in a way that allows me to add photos, and products for sale easily. The site should be very user friendly but clean and professional looking. I have uploaded our new company Logo and I would definitely like it used throughout the pages. Ideally, the site should display our Motto, Company Vision, Pictures of Products and Results of use of products, testimonials from customers, Video tutorials. I need to be able to capture email addresses for easy email blasts and customer data collection, contact info, links to social media accounts, and detailed analytics to track traffic etc. I also need direct links to my CoinPouch and email.

It appears my brief is unclear. This is our first site. So i would like it to be able to showcase and all my products. I would like the coding for easy changes after the site goes live. I am not super tech savvy, but would like to be able to add new products and track traffic. Please let me know if this still needs clarification.

```html
<!DOCTYPE html>
<html lang="en">
<head>
<meta charset="utf-8">
<title>Velvet Root Studio</title>
<link href="https://fonts.googleapis.com/css2?family=Didact+Gothic&family=Lato:ital,wght@0,400;0,700;1,400&family=Oswald:wght@400;500&display=swap" rel="stylesheet">
<style>
:root{
  --orange:#f28124;
  --brown:#55433f;
  --ink:#3a3a3a;
  --muted:#666;
  --line:#dcdcdc;
  --lilac:#c9b6cc;
  --white:#fff;
}
*{box-sizing:border-box;margin:0;padding:0}
html,body{width:866px;height:1200px;overflow:hidden;background:var(--white)}
body{position:relative;font-family:'Lato',sans-serif;color:var(--ink)}
.abs{position:absolute}
.top-rule{left:0;top:0;width:866px;height:3px;background:var(--orange)}
.brand{left:54px;top:12px;width:90px;text-align:center}
.brand-mark{width:40px;height:40px;border-radius:50%;background:var(--brown);margin:0 auto 6px}
.brand-name{font-family:'Didact Gothic',sans-serif;font-size:9px;color:var(--orange);line-height:1.15}
.connect{left:497px;top:16px;font-family:'Didact Gothic',sans-serif;font-size:10px;display:flex;align-items:center;gap:5px}
.connect span.dot{width:15px;height:15px;border-radius:50%;background:var(--orange);display:inline-block}
.mail{left:683px;top:16px;font-family:'Didact Gothic',sans-serif;font-size:9.5px;display:flex;align-items:center;gap:8px}
.head-rule{left:208px;top:43px;width:605px;height:1px;background:var(--line)}
.nav{left:209px;top:57px;height:27px;display:flex;align-items:center;font-family:'Didact Gothic',sans-serif;font-size:10px}
.nav a{color:var(--ink);text-decoration:none}
.nav .active{background:var(--orange);color:var(--white);width:59px;height:27px;line-height:27px;text-align:center}
.hero{left:54px;top:93px;width:759px;height:278px;border:3px solid var(--lilac);background:linear-gradient(90deg,#e7dbe7 0%,#ddcbdc 45%,#6b4a3c 62%,#3b2720 75%,#cfbfcf 100%)}
.hero-photo{position:absolute;right:0;top:0;width:420px;height:272px;background:linear-gradient(90deg,rgba(221,203,220,0) 0%,#7a5443 25%,#4a2f24 55%,#9a8a95 85%,#d8c9d8 100%)}
.motto{left:81px;top:158px;font-family:'Didact Gothic',sans-serif;font-size:20px;color:var(--orange)}
.headline{left:81px;top:181px;font-family:'Oswald',sans-serif;font-size:25px;line-height:28px;color:var(--ink);letter-spacing:-.3px}
.hero-btn{left:81px;top:252px;width:88px;height:26px;background:var(--orange);color:var(--white);font-family:'Oswald',sans-serif;font-size:14px;line-height:26px;text-align:center}
.dots{left:82px;top:338px;display:flex;gap:5px}
.dots i{width:7px;height:7px;border-radius:50%;background:var(--ink);display:block}
.vision-title{left:0;width:866px;top:390px;text-align:center;font-family:'Didact Gothic',sans-serif;font-size:20px}
.vision-text{left:68px;width:730px;top:424px;text-align:center;font-style:italic;font-size:8.6px;line-height:15.3px;color:var(--ink)}
.thanks{left:0;width:866px;top:526px;text-align:center;font-family:'Didact Gothic',sans-serif;font-size:13px;color:var(--orange)}
.rule{height:1px;background:var(--line)}
.sec-title{font-family:'Didact Gothic',sans-serif;font-size:20px;color:var(--ink)}
.card{width:156px;height:167px;border:1px solid var(--line);background:var(--white)}
.card .pic{position:absolute;left:30px;top:12px;width:96px;height:120px;background:linear-gradient(160deg,#e9e9e9,#cfcfcf)}
.card .label{position:absolute;left:-1px;right:-1px;bottom:-1px;height:28px;background:var(--orange);color:var(--white);font-family:'Didact Gothic',sans-serif;font-size:11px;line-height:28px;padding-left:11px}
.results{left:573px;top:617px;width:240px;height:167px;border:1px solid var(--line)}
.results .pic{position:absolute;left:15px;top:12px;width:70px;height:70px;background:linear-gradient(90deg,#6a4535,#8a5e48)}
.results .side{position:absolute;left:96px;top:11px;width:136px;font-size:9.5px;line-height:15.5px}
.results .under{position:absolute;left:15px;top:91px;width:220px;font-size:9.5px;line-height:15.5px}
.results .btn{position:absolute;left:15px;top:131px;width:100px;height:22px;background:var(--brown);color:var(--white);font-size:8.5px;line-height:22px;text-align:center;letter-spacing:.3px}
.quote{width:150px;font-style:italic;font-size:8.6px;line-height:15.3px;color:var(--muted)}
.quote b{font-style:normal;font-weight:700;color:#bbb;font-size:13px;line-height:8px;margin-right:3px}
.person{display:flex;align-items:center;gap:8px;font-family:'Didact Gothic',sans-serif;font-size:9.5px;color:var(--orange)}
.person i{width:38px;height:38px;border-radius:50%;background:linear-gradient(135deg,#5a3a2e,#a07866);display:block}
.read-all{left:54px;top:1010px;font-size:8.5px;letter-spacing:.2px}
.video{left:573px;top:866px;width:240px;height:157px;background:linear-gradient(100deg,#8a8a8a,#3a2a24 35%,#b9b9b9 70%,#d9d9d9)}
.footer{left:0;top:1068px;width:866px;height:132px;background:var(--brown)}
.news{left:54px;top:1038px;width:759px;height:61px;background:var(--orange);border:2px solid #e06e14}
.news-title{position:absolute;left:18px;top:17px;font-family:'Didact Gothic',sans-serif;font-size:19px;color:var(--white)}
.news-input{position:absolute;left:206px;top:9px;width:535px;height:40px;background:var(--white);font-family:'Didact Gothic',sans-serif;font-size:10px;color:var(--muted);padding:14px 0 0 14px}
.news-btn{position:absolute;left:642px;top:14px;width:92px;height:30px;background:var(--brown);color:var(--white);font-family:'Didact Gothic',sans-serif;font-size:12px;line-height:30px;text-align:center}
.foot-links{left:54px;top:1123px;font-family:'Didact Gothic',sans-serif;font-size:10px;color:var(--white);word-spacing:2px}
.copy{left:54px;top:1150px;font-family:'Didact Gothic',sans-serif;font-size:8.5px;line-height:15px;color:#9a8c88}
.pay{left:713px;top:1132px;width:100px;height:40px;background:#fdf0c8;border-radius:6px;text-align:center;font-family:'Didact Gothic',sans-serif;color:var(--brown)}
.pay small{display:block;font-size:6px;padding-top:6px;letter-spacing:.4px}
.pay span{display:block;font-size:15px;line-height:18px}
</style>
</head>
<body>
<div class="abs top-rule"></div>

<header>
  <div class="abs brand"><div class="brand-mark"></div><div class="brand-name">Velvet Root Studio</div></div>
  <div class="abs connect">Connect Us : <span class="dot"></span><span class="dot"></span><span class="dot"></span><span class="dot"></span><span class="dot"></span></div>
  <div class="abs mail">
    <svg width="16" height="11" viewBox="0 0 16 11"><rect x=".5" y=".5" width="15" height="10" fill="none" stroke="#3a3a3a"/><path d="M.5 .5 8 6.5 15.5 .5" fill="none" stroke="#3a3a3a"/></svg>
    hello@velvetroot.example
  </div>
  <div class="abs head-rule"></div>
  <nav class="abs nav">
    <a class="active" href="#">HOME</a>
    <a href="#" style="margin-left:30px">ABOUT US</a>
    <a href="#" style="margin-left:44px">PRODUCTS</a>
    <a href="#" style="margin-left:45px">TESTIMONIALS</a>
    <a href="#" style="margin-left:45px">VIDEOS</a>
    <a href="#" style="margin-left:44px">NEWS</a>
    <a href="#" style="margin-left:45px">CONTACT US</a>
  </nav>
</header>

<section class="abs hero">
  <div class="hero-photo" role="img" aria-label="Close-up photo of a smiling woman holding makeup brushes"></div>
</section>
<div class="abs motto">OUR MOTTO:</div>
<div class="abs headline">HEALTHY HAIR AND SKIN IS OUR PRIORITY....<br>A BEAUTIFUL YOU IS OUR SPECIALTY</div>
<div class="abs hero-btn">MORE INFO</div>
<div class="abs dots"><i></i><i></i><i></i><i></i></div>

<h2 class="abs vision-title" style="font-weight:400">Company Vision</h2>
<p class="abs vision-text">Velvet Root Studio was created based on over 15 years of experience working with clients of varying demographics &amp; needs. During this time it became obvious there was a sincere need for a company and line of products that are designed to care for hair and skin from the inside out without all of the harsh chemicals found in many popular products today. So many of us are making the decision to live a healthier, more natural lifestyle and are tired of spending countless dollars trying products that do NOT provide the full circle benefits needed. Velvet Root Studio would LOVE to be your relief from this frustration. Our products have been tested on various hair types from straight to curly wave patterns and a range of skin types to formulate the best possible product for you and your family. Our goal is to always listen to your needs as customers and provide a quality product that nourishes you and yours from the inside out all while making you feel beautiful.</p>
<div class="abs thanks">Thank you for Choosing Velvet Root Studio!</div>
<div class="abs rule" style="left:54px;top:562px;width:759px"></div>

<h2 class="abs sec-title" style="left:53px;top:582px;font-weight:400">Our Products</h2>
<div class="abs card" style="left:54px;top:617px"><div class="pic" role="img" aria-label="Product photo: cream jar and box"></div><div class="label">Product Name</div></div>
<div class="abs card" style="left:226px;top:617px"><div class="pic" role="img" aria-label="Product photo: orange bottle and tube"></div><div class="label">Product Name</div></div>
<div class="abs card" style="left:397px;top:617px"><div class="pic" role="img" aria-label="Product photo: powder compact"></div><div class="label">Product Name</div></div>

<h2 class="abs sec-title" style="left:572px;top:582px;font-weight:400">Products Results</h2>
<div class="abs results">
  <div class="pic" role="img" aria-label="Before and after skin result photo"></div>
  <p class="side">Aliquam molestie, mi et imperdiet euismod, dui purus auctor tellus, et interdum lacus lectus et ante accumsan sollicitudin sapien</p>
  <p class="under">Aliquam molestie, mi et imperdiet euismod, dui purus auctor tellus, et interdum lacus..</p>
  <div class="btn">VIEW ALL RESULTS</div>
</div>

<div class="abs rule" style="left:54px;top:811px;width:759px"></div>

<h2 class="abs sec-title" style="left:54px;top:830px;font-weight:400">Testimonials</h2>
<p class="abs quote" style="left:53px;top:864px"><b>&ldquo;</b>Aliquam molestie, mi et imperdiet euismod, dui purus auctor tellus, et interdum lacus lectus et ante. Sed accumsan sollicitudin sapien, sit amet adipiscing turpis...</p>
<p class="abs quote" style="left:222px;top:864px"><b>&ldquo;</b>Aliquam molestie, mi et imperdiet euismod, dui purus auctor tellus, et interdum lacus lectus et ante. Sed accumsan sollicitudin sapien, sit amet adipiscing turpis...</p>
<p class="abs quote" style="left:389px;top:864px"><b>&ldquo;</b>Aliquam molestie, mi et imperdiet euismod, dui purus auctor tellus, et interdum lacus lectus et ante. Sed accumsan sollicitudin sapien, sit amet adipiscing turpis...</p>
<div class="abs person" style="left:54px;top:951px"><i role="img" aria-label="Customer portrait"></i>Name Heading</div>
<div class="abs person" style="left:223px;top:951px"><i role="img" aria-label="Customer portrait"></i>Name Heading</div>
<div class="abs person" style="left:390px;top:951px"><i role="img" aria-label="Customer portrait"></i>Name Heading</div>
<div class="abs read-all">READ ALL TESTIMONIALS &raquo;</div>
<div class="abs" style="left:553px;top:834px;width:1px;height:186px;background:var(--line)"></div>

<h2 class="abs sec-title" style="left:573px;top:830px;font-weight:400">Video Tutorials</h2>
<div class="abs video" role="img" aria-label="Video still: makeup brush tutorial">
  <svg style="position:absolute;left:100px;top:58px" width="42" height="42" viewBox="0 0 42 42"><circle cx="21" cy="21" r="19" fill="rgba(0,0,0,.25)" stroke="#fff" stroke-width="2.5"/><path d="M16 12 31 21 16 30Z" fill="#fff"/></svg>
</div>

<footer class="abs footer"></footer>
<div class="abs news">
  <div class="news-title">Newsletter SignUp</div>
  <div class="news-input">Enter Email Address</div>
  <div class="news-btn">SIGN UP</div>
</div>
<div class="abs foot-links">Home&nbsp; / &nbsp;&nbsp;About Us&nbsp; / &nbsp;&nbsp;Products&nbsp; / &nbsp;&nbsp;Testimonials&nbsp; / &nbsp;&nbsp;Videos&nbsp; / &nbsp;&nbsp;News&nbsp; / &nbsp;&nbsp;Contact Us</div>
<div class="abs copy">Copyright &copy; 2015. Velvet Root Studio. All Right Reserved<br>Privacy Policy</div>
<div class="abs pay"><small>NOW ACCEPTING</small><span>CoinPouch</span></div>
</body>
</html>
```